175th Anniversary of Family Owned Funeral Home Pole Banners

We are family owned and operated funeral home in the Greater Cincinnati area and operate 3 funeral homes and a cremation center and we will be celebrating our 175th anniversary in 2015. The communities we serve look to us as leaders in the community and we are very well recognized. In preparation for next year, part of our planning includes placing pole banners in our local communities and our funeral home parking areas. The banner dimensions will be 30 x 60. We need for the banners to display a great message of tradition and excellence. Our website is www.brannockvelder.com I have uploaded an example of a pole banner as well as our logo(s).
Updates
Original artwork has been uploaded if needed.
Industry/Entity Type
Funeral Home

```html
<!DOCTYPE html>
<html lang="en">
<head>
<meta charset="utf-8">
<title>Brannock Velder 175th Anniversary Pole Banner</title>
<link href="https://fonts.googleapis.com/css2?family=Lora:ital,wght@0,400;1,400&display=swap" rel="stylesheet">
<style>
  :root {
    --page: #ffffff;
    --banner-navy: #2b2f6e;
    --ornament-tone: #3a3f80;
    --ink-white: #ffffff;
  }
  html, body {
    margin: 0;
    padding: 0;
    width: 1200px;
    height: 1000px;
    overflow: hidden;
    background: var(--page);
  }
  .canvas {
    position: relative;
    width: 1200px;
    height: 1000px;
  }
  .pole-banner {
    position: absolute;
    left: 0;
    top: 0;
  }
  .banner-body {
    fill: var(--banner-navy);
    filter: drop-shadow(0 6px 10px rgba(0,0,0,0.18));
  }
  .frame-line {
    fill: none;
    stroke: var(--ink-white);
    stroke-width: 1.6;
  }
  .corner-dot { fill: var(--ink-white); }
  .headline-script {
    font-family: "Lora", serif;
    font-style: italic;
    fill: var(--ink-white);
    text-anchor: middle;
  }
  .headline-our { font-size: 44px; }
  .headline-anniversary { font-size: 52px; }
  .medallion-oval {
    fill: var(--banner-navy);
    stroke: var(--ink-white);
  }
  .medallion-number {
    font-family: "Lora", serif;
    font-size: 66px;
    fill: var(--ink-white);
    text-anchor: middle;
  }
  .medallion-years {
    font-family: "Lora", serif;
    font-style: italic;
    font-size: 28px;
    fill: var(--ink-white);
    text-anchor: middle;
  }
  .brand-mark-spot { fill: var(--ink-white); }
  .brand-name {
    font-family: "Lora", serif;
    font-style: italic;
    font-size: 48px;
    fill: var(--ink-white);
    text-anchor: middle;
  }
  .brand-rule {
    stroke: var(--ink-white);
    stroke-width: 1.6;
  }
  .service-line {
    font-family: "Lora", serif;
    font-style: italic;
    font-size: 27px;
    fill: var(--ink-white);
    text-anchor: middle;
  }
</style>
</head>
<body>
<main class="canvas">
  <svg class="pole-banner" width="1200" height="1000" viewBox="0 0 1200 1000" xmlns="http://www.w3.org/2000/svg">
    <!-- banner field -->
    <rect class="banner-body" x="370" y="40" width="462" height="923"/>

    <!-- double frame -->
    <rect class="frame-line" x="382" y="52" width="438" height="899"/>
    <rect class="frame-line" x="389" y="59" width="424" height="885"/>

    <!-- corner dots -->
    <circle class="corner-dot" cx="401" cy="71" r="7"/>
    <circle class="corner-dot" cx="801" cy="71" r="7"/>
    <circle class="corner-dot" cx="401" cy="932" r="7"/>
    <circle class="corner-dot" cx="801" cy="932" r="7"/>

    <!-- headline -->
    <text class="headline-script headline-our" x="600" y="100">our</text>

    <!-- anniversary medallion -->
    <g class="medallion">
      <ellipse role="img" aria-label="Decorative scrollwork flourishes framing the anniversary medallion" cx="600" cy="215" rx="142" ry="98" fill="var(--ornament-tone)"/>
      <ellipse class="medallion-oval" cx="600" cy="218" rx="98" ry="62" stroke-width="6"/>
      <ellipse class="medallion-oval" cx="600" cy="218" rx="88" ry="53" stroke-width="2"/>
      <text class="medallion-number" x="600" y="236">175</text>
      <text class="medallion-years" x="600" y="262">years</text>
    </g>

    <text class="headline-script headline-anniversary" x="600" y="370">anniversary</text>

    <!-- brand mark placeholder -->
    <circle class="brand-mark-spot" cx="600" cy="565" r="70"/>

    <!-- brand name -->
    <text class="brand-name" x="600" y="818">Brannock Velder</text>
    <line class="brand-rule" x1="402" y1="846" x2="798" y2="846"/>

    <!-- services -->
    <text class="service-line" x="600" y="883">Family Funeral Homes</text>
    <text class="service-line" x="600" y="919">&amp; Cremation Center</text>
  </svg>
</main>
</body>
</html>
```